Private lender of mortgages and rent to own housing

need a website that reflects real estate especially mortgage lending and rent to own houses..
Sections as follows
Home About Types of mortgages Rent to own Contact us
Target Market(s)
consumers who require non traditonal mortgages
Industry/Entity Type
Mortgage
Coding
Coded - Design and coding required
Number of Pages Required
4 page
Font styles to use
Sans Serif
Colors
Designer to choose colors to be used in the design.
Requirements
Must have
- background pictures on pages. with nice picture on homepage of houses or a community
Nice to have
- contact us form i supplied a ink to

```html
<!DOCTYPE html>
<html lang="en">
<head>
<meta charset="utf-8">
<title>Lakeshore Lending Group – Private Mortgages &amp; Rent To Own</title>
<link href="https://fonts.googleapis.com/css2?family=Questrial&family=Arimo:wght@400;700&family=Montserrat:wght@500;600;700&display=swap" rel="stylesheet">
<style>
:root{
  --navy:#231f5e;
  --navy-dark:#1b1850;
  --text:#333;
  --muted:#666;
  --grey-bg:#f2f2f2;
  --line:#d6d6d6;
  --circle-grey:#9b9b9b;
  --copy-bar:#9a9a9a;
  --white:#fff;
  --red:#c0272d;
}
*{box-sizing:border-box;margin:0;padding:0}
html,body{width:1200px;height:2406px;overflow:hidden}
body{font-family:"Arimo",Arial,sans-serif;color:var(--text);background:var(--white);font-size:13px;line-height:1.6}
.wrap{width:918px;margin:0 auto;position:relative}
ul{list-style:none}

/* header */
.site-header{height:88px;border-top:4px solid var(--navy-dark)}
.site-header .wrap{display:flex;justify-content:space-between;align-items:center;height:84px}
.brand{display:flex;align-items:center;gap:10px;font-family:"Montserrat",sans-serif;font-weight:700;font-size:14px;color:var(--navy);letter-spacing:.2px}
.brand-mark{width:14px;height:14px;border-radius:50%;background:var(--navy)}
.header-contact{display:flex;align-items:center;gap:22px;font-size:13px;color:var(--text)}
.header-contact span{display:flex;align-items:center;gap:8px}
.header-contact .divider{width:1px;height:26px;background:var(--line)}

/* hero */
.hero{height:406px;position:relative;background:linear-gradient(180deg,#cfe0ee 0%,#e8eef2 40%,#9fae7c 78%,#5d6d3c 100%)}
.hero-photo{position:absolute;inset:0;background:linear-gradient(100deg,rgba(255,255,255,0) 35%,rgba(190,120,80,.35) 60%,rgba(230,230,225,.55) 80%,rgba(200,90,60,.3) 100%)}
.main-nav{position:absolute;top:3px;left:141px;width:918px;height:45px;background:rgba(200,200,200,.85);display:flex;align-items:center}
.main-nav a{font-family:"Montserrat",sans-serif;font-size:12px;font-weight:600;color:var(--white);text-decoration:none;letter-spacing:.5px;padding:0 0 0 0;display:block;text-align:center}
.nav-links{display:flex;height:45px;align-items:center;padding-left:8px}
.nav-links li{height:37px;display:flex;align-items:center;justify-content:center;border-right:1px solid rgba(255,255,255,.6)}
.nav-links li:last-child{border-right:none}
.nav-links li.active{background:var(--navy);width:112px;border-right:none}
.nav-links li.w1{width:112px}.nav-links li.w2{width:200px}.nav-links li.w3{width:165px}.nav-links li.w4{width:145px}
.nav-social{margin-left:auto;height:45px;width:135px;background:var(--navy);clip-path:polygon(8% 0,100% 0,100% 100%,0 100%);display:flex;align-items:center;justify-content:center;gap:22px}
.nav-social i{display:block;width:10px;height:10px;border-radius:50%;background:var(--white)}
.hero-copy{position:absolute;left:141px;top:125px;font-family:"Questrial",sans-serif;font-size:28px;line-height:1.3;color:var(--navy)}
.hero-copy strong{font-family:"Montserrat",sans-serif;font-weight:700;font-size:26px}
.hero-dots{position:absolute;left:141px;top:270px;display:flex;gap:9px}
.hero-dots i{width:7px;height:7px;background:var(--navy)}
.hero-dots i:last-child{background:var(--white)}

/* about */
.about{height:399px;padding-top:52px}
.about .wrap{display:flex;justify-content:space-between}
.about-text{width:616px}
.section-title{font-family:"Questrial",sans-serif;font-size:29px;color:var(--navy);font-weight:400;letter-spacing:.3px}
.section-title strong{font-family:"Montserrat",sans-serif;font-weight:700}
.about-text .section-title{padding-bottom:8px;border-bottom:1px solid var(--line);position:relative}
.about-text .section-title::after{content:"";position:absolute;left:0;bottom:-5px;width:8px;height:8px;background:var(--line)}
.lead{font-weight:700;font-size:14px;color:#222;margin-top:22px;line-height:1.5}
.about-text p.body{font-size:12.5px;color:var(--muted);margin-top:6px;line-height:1.65}
.btn{display:inline-flex;align-items:center;gap:10px;border:1px solid var(--line);padding:5px 0 5px 16px;font-family:"Montserrat",sans-serif;font-weight:700;font-size:11px;color:#222;letter-spacing:.5px;margin-top:18px;background:var(--white)}
.btn svg{margin-right:-1px}
.inquiry{width:262px;height:302px;border:1px solid var(--line);margin-top:-2px}
.inquiry-head{background:var(--navy);height:62px;clip-path:polygon(0 0,100% 0,100% 70%,50% 100%,0 70%);color:var(--white);text-align:center;font-family:"Montserrat",sans-serif;font-weight:600;font-size:18px;padding-top:4px}
.inquiry form{padding:8px 13px 0}
.field{border:1px solid var(--line);height:32px;margin-bottom:6px;font-size:11.5px;color:#555;padding:7px 8px}
.field b{color:var(--red);font-weight:400}
.field.msg{height:55px}
.inquiry .btn{margin-top:4px}

/* mortgage types */
.types{background:var(--grey-bg);height:786px;padding-top:50px}
.center-title{text-align:center;position:relative}
.center-title::after{content:"";display:block;width:487px;height:1px;background:var(--line);margin:6px auto 0}
.center-title::before{content:"";position:absolute;left:50%;bottom:-4px;width:8px;height:8px;margin-left:-4px;background:var(--line)}
.tabs{display:flex;margin-top:26px;height:157px}
.tab{width:213px;text-align:center;padding-top:20px;font-family:"Questrial",sans-serif;font-weight:700;font-size:16px;color:#222}
.tab svg{display:block;margin:0 auto 14px}
.tab.active{background:var(--white);border:2px solid #ddd;border-bottom:none;border-radius:8px 8px 0 0;position:relative;z-index:1;margin-bottom:-2px}
.tab:nth-child(2){width:231px}.tab:nth-child(3){width:230px}.tab:nth-child(4){width:244px}
.tab-panel{background:var(--white);border:2px solid #ddd;border-radius:0 8px 8px 8px;height:451px;padding:22px 26px}
.tab-panel .q{font-family:"Questrial",sans-serif;font-size:14.5px;color:#222;line-height:1.5}
.tab-panel .note{font-size:12px;color:var(--muted);margin-top:8px}
.block-head{display:flex;align-items:center;gap:10px;margin-top:40px;font-family:"Questrial",sans-serif;font-size:18px;color:var(--navy)}
.block-head.sol{margin-top:26px}
.points{margin:8px 0 0 44px}
.points li{font-size:12px;color:var(--muted);position:relative;padding-left:16px;margin-bottom:4px;line-height:1.55}
.points li::before{content:"›";position:absolute;left:0;top:-1px;font-size:14px}
.points.sol li{margin-bottom:12px}

/* rent to own */
.rent{height:474px;padding-top:52px;text-align:center}
.rent .center-title::after{width:376px}
.rent-intro{font-family:"Questrial",sans-serif;font-size:15px;color:#222;margin:30px auto 0;width:940px;line-height:1.4}
.steps{display:flex;justify-content:center;gap:63px;margin-top:22px;margin-left:-12px}
.step{width:133px;font-family:"Montserrat",sans-serif;font-weight:600;font-size:15px;color:var(--circle-grey)}
.step .ring{width:133px;height:133px;border-radius:50%;border:1px solid #bbb;padding:5px}
.step .disc{width:100%;height:100%;border-radius:50%;background:var(--circle-grey);display:flex;align-items:center;justify-content:center}
.step.active{color:var(--navy)}
.step.active .ring{border-color:var(--navy)}
.step.active .disc{background:var(--navy)}
.step span{display:inline-block;margin-top:8px;padding-bottom:8px}
.step.active span{border-bottom:2px solid var(--navy)}
.rent-detail{font-size:12.5px;color:#444;width:918px;margin:14px auto 0;line-height:1.6}

/* footer */
.site-footer{background:var(--navy);height:216px;color:var(--white)}
.site-footer .wrap{display:flex;padding-top:36px}
.foot-title{font-family:"Questrial",sans-serif;font-size:15px;font-weight:400;letter-spacing:.3px;padding-bottom:6px;border-bottom:1px solid rgba(255,255,255,.5)}
.foot-title strong{font-family:"Montserrat",sans-serif;font-weight:700}
.quick{width:185px}
.quick .foot-title{width:112px}
.quick ul{margin-top:12px;padding-left:16px}
.quick li{font-size:11.5px;line-height:1.65;list-style:disc}
.contact{width:260px}
.contact .foot-title{width:198px}
.contact h4{font-family:"Montserrat",sans-serif;font-size:11.5px;font-weight:700;margin-top:14px}
.contact p{display:flex;align-items:center;gap:8px;font-size:11.5px;margin-top:6px}
.contact p.mail{margin-top:18px}
.map{width:212px;height:129px;margin-top:8px;border:3px solid var(--white);background:linear-gradient(120deg,#e6e3da 0%,#dcd8cc 45%,#a9d3ee 55%,#9fcbe8 100%)}
.foot-brand{margin-left:auto;text-align:center;width:201px;padding-top:60px}
.foot-brand .brand{color:var(--white);justify-content:center;font-size:13px}
.foot-brand .brand-mark{background:var(--white)}
.foot-social{display:flex;justify-content:center;gap:21px;margin-top:22px}
.foot-social i{width:24px;height:24px;border-radius:50%;border:2px solid var(--white);background:#2f8fd6}
.copyright{background:var(--copy-bar);height:37px;text-align:center;color:var(--white);font-size:11px;line-height:37px}
</style>
</head>
<body>

<header class="site-header">
  <div class="wrap">
    <div class="brand"><span class="brand-mark"></span>LAKESHORE LENDING GROUP</div>
    <div class="header-contact">
      <span><svg width="14" height="18" viewBox="0 0 14 18"><path d="M7 1a6 6 0 0 1 6 6c0 4-6 10-6 10S1 11 1 7a6 6 0 0 1 6-6z" fill="none" stroke="#231f5e" stroke-width="1.5"/><circle cx="7" cy="7" r="2" fill="#231f5e"/></svg>Pinecrest Ontario</span>
      <i class="divider"></i>
      <span><svg width="20" height="16" viewBox="0 0 20 16"><rect x="1" y="4" width="18" height="11" fill="none" stroke="#231f5e" stroke-width="1.4"/><path d="M1 4l9 6 9-6M4 4V1h12v3" fill="none" stroke="#231f5e" stroke-width="1.4"/></svg>hello@lakeshorelending.ca</span>
    </div>
  </div>
</header>

<section class="hero">
  <div class="hero-photo" role="img" aria-label="Photo of a smiling family standing in front of a suburban house with solar panels on the roof"></div>
  <nav class="main-nav">
    <ul class="nav-links">
      <li class="active"><a href="#">HOME</a></li>
      <li class="w1"><a href="#">ABOUT US</a></li>
      <li class="w2"><a href="#">TYPES OF MORTGAGES</a></li>
      <li class="w3"><a href="#">RENT TO OWN</a></li>
      <li class="w4"><a href="#">CONTACT US</a></li>
    </ul>
    <div class="nav-social"><i></i><i></i><i></i></div>
  </nav>
  <h1 class="hero-copy">We Are A <strong>Private Lender Of<br>Mortgages</strong> And We Provide<br><strong>Rent To Own Housing.</strong></h1>
  <div class="hero-dots"><i></i><i></i><i></i></div>
</section>

<section class="about">
  <div class="wrap">
    <div class="about-text">
      <h2 class="section-title">ABOUT <strong>LAKESHORE LENDING GROUP</strong></h2>
      <p class="lead">Lakeshore Lending Group is a private lender of 1st,2nd, construction and bridge mortgages in Pinecrest County area.</p>
      <p class="body">LLG offers a wide array of financing options to provide assistance to those of you that do not meet the bank's criteria. The reasons could range from bruised credit to inability to provide the banks with the required documentation to meet income qualification guidelines or simply you need a short term solution and the bank isn't an option. We are here to help in any way that we can. Please email an outline of your situation and we will analyze it and forward to one of our associated licensed mortgage brokers to contact you and start the process! We Can Put You in Your Own Home Today We know life sometimes delivers challenges and it can be hard to get back on track once you have dealt with challenges.</p>
      <a class="btn">READ MORE <svg width="26" height="22" viewBox="0 0 26 22"><path d="M1 21V9l12-8 12 8v12z" fill="#fff" stroke="#ccc"/><rect x="9" y="11" width="3" height="3" fill="#ccc"/><rect x="14" y="11" width="3" height="3" fill="#ccc"/><rect x="9" y="15" width="3" height="3" fill="#ccc"/><rect x="14" y="15" width="3" height="3" fill="#ccc"/></svg></a>
    </div>
    <aside class="inquiry">
      <div class="inquiry-head">Quick Inquiry</div>
      <form>
        <div class="field">Name<b>*</b></div>
        <div class="field">Email<b>*</b></div>
        <div class="field">Phone<b>*</b></div>
        <div class="field msg">Message<b>*</b></div>
        <a class="btn">SUBMIT <svg width="26" height="22" viewBox="0 0 26 22"><path d="M1 21V9l12-8 12 8v12z" fill="#fff" stroke="#ccc"/><rect x="9" y="11" width="3" height="3" fill="#ccc"/><rect x="14" y="11" width="3" height="3" fill="#ccc"/><rect x="9" y="15" width="3" height="3" fill="#ccc"/><rect x="14" y="15" width="3" height="3" fill="#ccc"/></svg></a>
      </form>
    </aside>
  </div>
</section>

<section class="types">
  <div class="wrap">
    <h2 class="section-title center-title">TYPES OF <strong>MORTGAGES WE DO</strong></h2>
    <div class="tabs">
      <div class="tab active">
        <svg width="64" height="56" viewBox="0 0 64 56"><path d="M2 38L17 26l15 12v16H2z" fill="#231f5e"/><rect x="13" y="42" width="8" height="12" fill="#fff"/><path d="M34 16L47 5l13 11v14H34z" fill="#231f5e"/><rect x="43" y="20" width="7" height="10" fill="#fff"/><path d="M30 40l12-8" stroke="#999" stroke-width="3"/><path d="M38 29l6 1-2 6z" fill="#999"/></svg>
        Bridge Financing
      </div>
      <div class="tab">
        <svg width="76" height="62" viewBox="0 0 76 62"><path d="M38 4v48M14 12h48" stroke="#231f5e" stroke-width="3"/><path d="M14 12L4 34h20zM62 12l-10 22h20z" fill="none" stroke="#231f5e" stroke-width="2"/><path d="M4 34a10 6 0 0 0 20 0zM52 34a10 6 0 0 0 20 0z" fill="#231f5e"/><rect x="26" y="52" width="24" height="5" fill="#231f5e"/><circle cx="60" cy="50" r="9" fill="#999"/></svg>
        Debt Consolidation
      </div>
      <div class="tab">
        <svg width="64" height="62" viewBox="0 0 64 62"><path d="M4 40L20 26l16 14v20H4z" fill="#231f5e"/><rect x="16" y="46" width="8" height="14" fill="#fff"/><path d="M22 22a16 16 0 0 1 22-10" fill="none" stroke="#999" stroke-width="4"/><path d="M42 6l8 6-9 4z" fill="#999"/><text x="50" y="28" font-family="Arimo,sans-serif" font-size="18" fill="#999">$</text></svg>
        Equity Take Out
      </div>
      <div class="tab">
        <svg width="72" height="62" viewBox="0 0 72 62"><path d="M4 36L24 18l20 18v24H4z" fill="#231f5e"/><rect x="19" y="44" width="10" height="16" fill="#fff"/><circle cx="52" cy="18" r="14" fill="none" stroke="#999" stroke-width="2"/><text x="46" y="25" font-family="Arimo,sans-serif" font-size="18" fill="#999">$</text></svg>
        Construction Financing
      </div>
    </div>
    <div class="tab-panel">
      <p class="q">Are you or your client looking forward to moving into that new property you just purchased, but your possession date is earlier than the sale of your current property?</p>
      <p class="note">Often, possession dates don't align in a way that is most convenient, and our bridge financing option will provide the peace of mind while in transition.</p>
      <h3 class="block-head"><svg width="22" height="20" viewBox="0 0 22 20"><rect x="1" y="1" width="8" height="8" fill="#231f5e"/><rect x="11" y="1" width="8" height="8" fill="none" stroke="#231f5e" stroke-width="2"/><rect x="1" y="11" width="8" height="8" fill="none" stroke="#231f5e" stroke-width="2"/><path d="M15 11v8M12 16l3 3 3-3" stroke="#231f5e" stroke-width="2" fill="none"/></svg>Problem:</h3>
      <ul class="points">
        <li>Loans are often too short term</li>
        <li>You don't want to lose the sales of your property while waiting for financing</li>
        <li>Existing lenders are not willing or able to bridge the purchase with your existing equity</li>
        <li>Limited and restrictive conditions cause penalties at traditional financial institutions</li>
        <li>Your house is listed but hasn't sold yet</li>
      </ul>
      <h3 class="block-head sol"><svg width="22" height="22" viewBox="0 0 22 22"><circle cx="11" cy="10" r="5" fill="#231f5e"/><rect x="9" y="15" width="4" height="4" fill="#231f5e"/><path d="M11 0v3M2 10h3M17 10h3M4 3l2 2M18 3l-2 2" stroke="#231f5e" stroke-width="1.6"/></svg>Solution:</h3>
      <ul class="points sol">
        <li>We can help you close the sale of your purchase before the property you are moving out of sells, or before its possession date if it is sold. We offer a short term loan to bridge the gap for you, allowing a less stressful transition between homes.</li>
        <li>We can also help you take advantage of your prepayment privileges on the house you are selling to help reduce your prepayment penalty.</li>
      </ul>
    </div>
  </div>
</section>

<section class="rent">
  <h2 class="section-title center-title">RENT TO <strong>OWN A HOME</strong></h2>
  <p class="rent-intro">We Can Put You in Your Own Home Today We know life sometimes delivers challenges and it can be hard to get back on track once you have dealt with challenges.</p>
  <div class="steps">
    <div class="step active">
      <div class="ring"><div class="disc"><svg width="40" height="48" viewBox="0 0 40 48"><path d="M14 2h12l-4 8h-4z" fill="#fff"/><path d="M16 11h8c10 6 14 16 14 24 0 8-6 11-18 11S2 43 2 35c0-8 4-18 14-24z" fill="#fff"/><text x="13" y="39" font-family="Arimo,sans-serif" font-weight="700" font-size="20" fill="#231f5e">$</text></svg></div></div>
      <span>Down payment</span>
    </div>
    <div class="step">
      <div class="ring"><div class="disc"><svg width="54" height="46" viewBox="0 0 54 46"><path d="M2 22L27 2l25 20" fill="none" stroke="#fff" stroke-width="3"/><path d="M8 20v24h38V20" fill="none" stroke="#fff" stroke-width="3"/><rect x="18" y="24" width="18" height="14" fill="#fff"/></svg></div></div>
      <span>Household Income</span>
    </div>
    <div class="step">
      <div class="ring"><div class="disc"><svg width="44" height="50" viewBox="0 0 44 50"><path d="M4 2h22l8 8v36H4z" fill="#fff"/><path d="M10 16h18M10 22h18M10 28h12" stroke="#9b9b9b" stroke-width="2"/><circle cx="32" cy="38" r="10" fill="#fff" stroke="#9b9b9b" stroke-width="2"/><path d="M27 38l4 4 6-7" stroke="#9b9b9b" stroke-width="2.5" fill="none"/></svg></div></div>
      <span>Credit Report</span>
    </div>
    <div class="step">
      <div class="ring"><div class="disc"><svg width="50" height="48" viewBox="0 0 50 48"><path d="M12 18L26 6l14 12v12H12z" fill="#fff"/><rect x="23" y="22" width="6" height="8" fill="#9b9b9b"/><path d="M2 34c8-2 14 2 20 3h10c3 0 3 4 0 4H20M2 44h30l14-10c2-2 0-5-3-3l-9 5" fill="none" stroke="#fff" stroke-width="3"/></svg></div></div>
      <span>Selecting a House</span>
    </div>
  </div>
  <p class="rent-detail">We require a minimum down payment of $10,000 or 3.5% to 4% of total price of the home (whichever is larger).&nbsp;&nbsp; So a $400,000 will require a bigger down than a $300,000 house. This is 100% credited towards your purchase of the home. Your down payment is required at the time we have the home inspection.</p>
</section>

<footer class="site-footer">
  <div class="wrap">
    <div class="quick">
      <h4 class="foot-title">QUICK <strong>LINKS</strong></h4>
      <ul>
        <li>Home</li>
        <li>About Us</li>
        <li>Types Of Mortgages</li>
        <li>Rent To Own</li>
        <li>Contact Us</li>
      </ul>
    </div>
    <div class="contact">
      <h4 class="foot-title">CONTACT <strong>DETAILS</strong></h4>
      <h4>LAKESHORE LENDING GROUP</h4>
      <p><svg width="11" height="14" viewBox="0 0 14 18"><path d="M7 1a6 6 0 0 1 6 6c0 4-6 10-6 10S1 11 1 7a6 6 0 0 1 6-6z" fill="none" stroke="#fff" stroke-width="1.6"/><circle cx="7" cy="7" r="2" fill="#fff"/></svg>Pinecrest Ontario</p>
      <p class="mail"><svg width="15" height="12" viewBox="0 0 20 16"><rect x="1" y="4" width="18" height="11" fill="none" stroke="#fff" stroke-width="1.6"/><path d="M1 4l9 6 9-6" fill="none" stroke="#fff" stroke-width="1.6"/></svg>hello@lakeshorelending.ca</p>
    </div>
    <div class="map" role="img" aria-label="Street map of the town centre beside the lake bay"></div>
    <div class="foot-brand">
      <div class="brand"><span class="brand-mark"></span>LAKESHORE LENDING GROUP</div>
      <div class="foot-social"><i></i><i></i><i></i></div>
    </div>
  </div>
</footer>
<div class="copyright">Copyright © 2017 LAKESHORE LENDING GROUP. All Rights Reserved</div>

</body>
</html>
```